Harbor Petroleum Business Cards

I would like to design some options for about 10 sets of double sided business cards for our team with a raised logo with a Silver glossy finished logo. We are a privately funded upstream Oil & Gas producer drilling vertical wells in Central Oklahoma with a long term production (ROI driven) strategy that we implement through an annual drilling program. We are focused on a shallow / vertical / long life / low decline strategy. We are based in downtown Tulsa Oklahoma. I have attached a sample business card and a picture of our hallway logo which we would like to replicate on the business cards.

Target Market(s)

SEC Accredited Investors and other Oil & Gas Operators

Industry/Entity Type

Upstream Oil & Gas

Contact Information for Business Card

You can see the sample photo attached, but email / website / address / direct phone / Cell Phone / Name / Title / Fax

Font styles to use
Other font styles liked:
• Felix Titling

Colors
0054AA
0677BA
7BADD7
CADEEF
E8F1F8

Requirements
Must have
• Glossy raised logo
Nice to have
• Possibly a new logo.
Should not have
• No Greens /

```html
<!DOCTYPE html>
<html lang="en">
<head>
<meta charset="utf-8">
<title>Harbor Petroleum Business Cards</title>
<link rel="stylesheet" href="https://fonts.googleapis.com/css2?family=Open+Sans:wght@400;700&display=swap">
<style>
  :root {
    --stage: #e9e6e1;
    --card-blue: #2b52a0;
    --card-blue-deep: #244890;
    --silver: #d4d8df;
    --white: #ffffff;
    --pale: #e8f1f8;
  }
  * { box-sizing: border-box; margin: 0; padding: 0; }
  html, body { width: 1200px; height: 900px; overflow: hidden; }
  body {
    background: var(--stage);
    font-family: "Open Sans", Arial, sans-serif;
    display: flex;
    align-items: center;
    justify-content: center;
    gap: 40px;
  }
  .card {
    position: relative;
    width: 540px;
    height: 309px;
    background: linear-gradient(160deg, var(--card-blue), var(--card-blue-deep));
    color: var(--white);
    box-shadow: 0 6px 18px rgba(0,0,0,.18);
  }
  .brand {
    display: flex;
    align-items: center;
    gap: 14px;
    font-family: "Open Sans", Arial, sans-serif;
    font-weight: 400;
    color: var(--silver);
    letter-spacing: .03em;
    white-space: nowrap;
  }
  .brand-mark {
    flex: none;
    border-radius: 50%;
    background: var(--silver);
  }
  /* back side */
  .card-back .brand {
    position: absolute; left: 50%; top: 82px;
    transform: translateX(-50%);
    font-size: 26px;
  }
  .card-back .brand-mark { width: 52px; height: 52px; }
  .card-back .web-contacts {
    position: absolute; left: 0; right: 0; top: 162px;
    text-align: center; font-size: 14px; line-height: 1.6;
    color: var(--pale);
  }
  /* front side */
  .card-front .brand {
    position: absolute; left: 40px; top: 50px;
    font-size: 21px;
  }
  .card-front .brand-mark { width: 42px; height: 42px; }
  .phone-list {
    position: absolute; right: 26px; top: 46px;
    list-style: none; font-size: 13px; line-height: 1.45;
  }
  .phone-list li { display: flex; align-items: center; gap: 6px; }
  .phone-icon { width: 12px; height: 12px; }
  .person {
    position: absolute; left: 36px; top: 170px;
  }
  .person-name {
    font-weight: 700; font-size: 19px; letter-spacing: .05em;
  }
  .person-title {
    font-size: 11.5px; line-height: 1.35; letter-spacing: .04em;
    text-transform: uppercase; margin-top: 4px; color: var(--pale);
  }
  .address {
    position: absolute; left: 36px; right: 20px; bottom: 30px;
    font-size: 13.5px; letter-spacing: .05em; text-transform: uppercase;
    text-align: right;
  }
</style>
</head>
<body>
  <section class="card card-back">
    <div class="brand"><span class="brand-mark"></span>Harbor Petroleum, LLC</div>
    <div class="web-contacts">
      <p>DTV@HPTulsa.com</p>
      <p>www.HarborPetroleumLLC.com</p>
    </div>
  </section>

  <section class="card card-front">
    <div class="brand"><span class="brand-mark"></span>Harbor Petroleum, LLC</div>
    <ul class="phone-list">
      <li><svg class="phone-icon" viewBox="0 0 12 12"><rect width="12" height="12" fill="#fff"/><path d="M3 2.5 L4.6 2.5 L5.2 4.3 L4.3 5 Q5.2 6.9 7 7.7 L7.7 6.8 L9.5 7.4 L9.5 9 Q5 9.2 3 4 Z" fill="#2b52a0"/></svg>539-555-0142</li>
      <li><svg class="phone-icon" viewBox="0 0 12 12"><rect width="12" height="12" fill="#fff"/><rect x="3" y="4" width="6" height="5" fill="#2b52a0"/><rect x="4" y="2.5" width="4" height="2" fill="#2b52a0"/></svg>918-555-0187</li>
      <li><svg class="phone-icon" viewBox="0 0 12 12"><rect width="12" height="12" fill="#fff"/><rect x="4" y="2" width="4" height="8" rx="1" fill="#2b52a0"/></svg>918-555-0163</li>
    </ul>
    <div class="person">
      <h1 class="person-name">DORIAN T. VASQUELL, CPL</h1>
      <p class="person-title">Executive Vice President Land,<br>Legal &amp; Business Development</p>
    </div>
    <p class="address">42, West 9th St, Suite 1100, Tulsa, OK 74119</p>
  </section>
</body>
</html>
```